Business Card Design Project

Design business card based on logo provided.

Industry/Entity Type

Business

Requirements
Nice to have
• Logo to be provided.

Solid green second side with reverse logo (buildings only, not text).

Because the logo is linear I think that it might be possible to extend the logo lines across the card (only on the second side) as an interesting design element.

"Guiding Clients Toward Smarter Project Delivery"

"Job Order Contracting and Best Value Specialist"

"Cooperation - Innovation - Efficiency"

Basic Info:
Nora Whitfield
Owner/Founder
505-718-6024
nora@norawhitfieldpartners.example

www.norawhitfieldpartners.example (this should probably be on reverse)

```html
<!DOCTYPE html>
<html lang="en">
<head>
<meta charset="utf-8">
<title>Nora Whitfield Partners — Business Card</title>
<link rel="stylesheet" href="https://fonts.googleapis.com/css2?family=Arimo:wght@400;700&family=Oswald:wght@400&display=swap">
<style>
  :root {
    --green: #7a9a2e;
    --green-light: #8fb03a;
    --green-text: #7ea332;
    --ink: #3a3a3a;
    --paper: #ffffff;
    --paper-shade: #f1f1f1;
    --backdrop: #e4e4e4;
  }
  * { box-sizing: border-box; margin: 0; padding: 0; }
  html, body { width: 1200px; height: 880px; overflow: hidden; }
  body {
    background: var(--backdrop);
    font-family: "Arimo", Arial, sans-serif;
    position: relative;
  }
  .card {
    position: absolute;
    top: 290px;
    width: 525px;
    height: 300px;
    box-shadow: 0 6px 18px rgba(0,0,0,0.18);
    overflow: hidden;
  }
  /* Front side */
  .card-front {
    left: 50px;
    background: linear-gradient(135deg, var(--paper) 40%, var(--paper-shade));
  }
  .brand {
    position: absolute;
    top: 36px;
    right: 36px;
    display: flex;
    align-items: center;
    gap: 10px;
  }
  .brand-mark {
    width: 14px;
    height: 14px;
    background: var(--green);
  }
  .brand-name {
    font-family: "Oswald", "Arial Narrow", sans-serif;
    font-weight: 400;
    font-size: 22px;
    line-height: 1.2;
    letter-spacing: 0.5px;
    color: var(--ink);
    text-transform: uppercase;
  }
  .contact {
    position: absolute;
    left: 40px;
    top: 104px;
  }
  .contact-name {
    font-size: 22px;
    font-weight: 700;
    color: var(--green-text);
  }
  .contact-title {
    font-size: 12px;
    color: var(--ink);
    margin: 4px 0 12px;
  }
  .contact-list { list-style: none; font-size: 12px; color: var(--ink); line-height: 1.55; }
  .contact-list .label { color: var(--green-text); font-weight: 700; margin-right: 4px; }
  .tagline-band {
    position: absolute;
    left: 0; right: 0; bottom: 0;
    height: 62px;
    background: var(--green);
    display: flex;
    align-items: flex-end;
    justify-content: center;
    padding-bottom: 14px;
  }
  .tagline-band::before {
    content: "";
    position: absolute;
    left: 0; right: 0; top: 0;
    height: 18px;
    background: var(--green-light);
  }
  .tagline {
    position: relative;
    color: var(--paper);
    font-size: 14px;
    font-weight: 700;
    white-space: nowrap;
  }
  /* Back side */
  .card-back {
    left: 625px;
    background: linear-gradient(160deg, var(--green-light), var(--green));
  }
  .back-brand {
    position: absolute;
    right: 34px;
    bottom: 62px;
    font-family: "Oswald", "Arial Narrow", sans-serif;
    font-weight: 400;
    font-size: 34px;
    line-height: 1.2;
    letter-spacing: 0.5px;
    color: var(--paper);
    text-transform: uppercase;
    white-space: nowrap;
  }
  .back-web {
    position: absolute;
    right: 36px;
    bottom: 34px;
    font-size: 13px;
    color: var(--paper);
  }
</style>
</head>
<body>
  <section class="card card-front" aria-label="Business card front">
    <div class="brand">
      <span class="brand-mark"></span>
      <span class="brand-name">Nora Whitfield Partners</span>
    </div>
    <div class="contact">
      <p class="contact-name">Nora Whitfield</p>
      <p class="contact-title">Owner/Founder</p>
      <ul class="contact-list">
        <li><span class="label">p:</span>505-718-6024</li>
        <li><span class="label">e:</span>nora@norawhitfieldpartners.example</li>
        <li><span class="label">w:</span>www.norawhitfieldpartners.example</li>
      </ul>
    </div>
    <div class="tagline-band">
      <p class="tagline">Guiding Clients Toward Smarter Project Delivery</p>
    </div>
  </section>

  <section class="card card-back" aria-label="Business card back">
    <p class="back-brand">Nora Whitfield Partners</p>
    <p class="back-web">www.norawhitfieldpartners.example</p>
  </section>
</body>
</html>
```